Hair and Grooming Salon Flyer

I need a double sided flyer to promote 2 services provided by 2 individual professionals in our salon (one offer per side?)

1. A MALE "POWER HOUR" (75mins of serious grooming) with Brenna
Choose any 2 male treatments from the following menus for just $99!
BODY
-30 minute deep tissue massage
-full body detox body scrub
-Mens maintenance pedicure
-Mens maintenance manicure
FACE
- Express Deep Cleanse Facial
- Microdermabrasion
- 30 minute Indian head massage
MANSCAPING
-Back and shoulder wax
-Chest and Stomach
-Mens Basic bikini (speedo line)
-1/2 leg wax

2. MARLOWS "COLOUR BAR" (available Tues - Thurs) $99
Freshen up your look in the experienced hands of a Senior Stylist
1/2 head of foils or regrowth colour
Precision style cut and Blowdry
Appointments after 4pm - enjoy a complimentry glass of wine

The design should communicate experience and confidence with a sense of specialty
Our colours are black white silver grey with bright orange accents

Terms & conditions
Offer 1. Offered by appointment with Brenna our Male grooming therapist only various days and times subject to availability, subject to change without notice; limitless services per customer

Offer 2. Available for limited times - Sept 16 - Nov 6 2014; Dec 30-Feb 27 with Marlow only and for one service per customer at advertised price of $99
Updates

Project Deadline Extended
Reason: One of my photos was not uploaded correctly and two photos of the same person was (to give choice) therefore the design for COLOUR BAR is incorrect. The photograph of the woman with short blonde hair is the hairdresser I wish to feature in the flyer for the COLOUR BAR My apologies

Target Market(s)

New clients! offer 1 - men, professionals / offer 2 - young adult women funky hair

Industry/Entity Type

Salon

Requirements
Must have
• Must have one offer per side of flyer
Must have photo shots of Brenna (2 provided, the second and third, you choose which is best) and of Marlow (first photo short blonde hair)
We have an extremely localised and personalised business but we need more clients for colour work so this is an introductory offer for hairdressing
and more male clients for Brenna who had an inner city practice with a large male clientele this will be an ongoing package on our menu

www.velquorastudio.net.au for look and feel of salon
and contact details
Should not have
• dont want to appear cheap or discounted - just packaged intelligently

```html
<!DOCTYPE html>
<html lang="en">
<head>
<meta charset="utf-8">
<title>Velquora Salon Flyers</title>
<link href="https://fonts.googleapis.com/css2?family=Roboto:wght@300;400;500;700;900&family=Roboto+Condensed:wght@400;700&display=swap" rel="stylesheet">
<style>
:root{
  --orange:#f26f21;
  --black:#000;
  --ink:#1b1b1b;
  --white:#fff;
  --paper:#f4f3f0;
  --footer:#ececec;
  --grey:#555;
  --stage:#d9d9d9;
  --photo-warm:#8a6a55;
  --photo-cool:#5a4a4a;
}
*{margin:0;padding:0;box-sizing:border-box}
html,body{width:1200px;height:1000px;overflow:hidden;background:var(--stage)}
body{position:relative;font-family:"Roboto",Arial,sans-serif}
.flyer{position:absolute;left:274px;width:826px;height:585px;transform:scale(.79);transform-origin:top left;background:var(--paper);box-shadow:0 3px 10px rgba(0,0,0,.25)}
.flyer--power{top:22px}
.flyer--colour{top:510px}
.panel{position:absolute;left:20px;top:20px;width:786px;height:405px;background:var(--black);border-radius:12px;overflow:hidden}
.footer{position:absolute;left:20px;top:425px;width:786px;height:140px;background:var(--footer)}
.abs{position:absolute;line-height:1;white-space:nowrap}
.head-thin{font-weight:300;color:var(--white);letter-spacing:-.02em}
.head-big{font-weight:500;color:var(--orange);letter-spacing:-.06em}
.small-note{font-size:12px;color:var(--white)}
.price{font-weight:500;color:var(--orange);letter-spacing:-.06em}
.price sup{font-size:.45em;vertical-align:top;position:relative;top:.15em}
.ornament{position:absolute;background:radial-gradient(ellipse at 55% 45%,rgba(242,111,33,.85),rgba(242,111,33,.35) 55%,rgba(242,111,33,0) 72%)}
.photo{position:absolute;border-radius:14px;border:4px solid var(--white);box-shadow:0 0 0 3px #999}
.badge{position:absolute;border-radius:50%;background:var(--white);border:7px solid var(--orange);text-align:center;color:var(--black)}
.menu-box{position:absolute;background:var(--orange);color:var(--white)}
.menu-title{position:absolute;left:16px;font-size:16px;font-weight:500}
.menu-items{position:absolute;left:16px;font-size:13.5px;line-height:17px}
.benefits{position:absolute;font-family:"Roboto Condensed",Arial,sans-serif;color:var(--white);list-style:none}
.benefits li{position:relative;padding-left:12px}
.benefits li::before{content:"";position:absolute;left:0;top:7px;width:6px;height:6px;border-radius:50%;background:var(--orange)}
.brand-name{position:absolute;left:37px;top:12px;font-size:31px;font-weight:500;color:var(--ink);line-height:1}
.address{position:absolute;left:37px;top:56px;font-size:13px;color:var(--grey);line-height:17px}
.phone{position:absolute;left:37px;top:94px;font-size:18px;font-weight:700;color:var(--orange)}
.email{position:absolute;left:37px;top:117px;font-size:14px;color:var(--grey)}
.email b{color:var(--ink);font-weight:500}
.divider{position:absolute;left:262px;top:20px;width:1px;height:108px;background:#bbb}
.hours{position:absolute;left:278px;top:12px;font-family:"Roboto Condensed",Arial,sans-serif;color:var(--ink);font-size:14px;line-height:18px}
.hours h3{color:var(--orange);font-size:15px;font-weight:700;margin-bottom:2px}
.hours .closed{margin-top:5px}
</style>
</head>
<body>

<section class="flyer flyer--power">
  <div class="panel">
    <div class="abs head-thin" style="left:68px;top:30px;font-size:42px">A male</div>
    <div class="abs head-big" style="left:52px;top:82px;font-size:84px">power</div>
    <div class="abs head-big" style="left:88px;top:146px;font-size:84px">hour</div>
    <div class="abs small-note" style="left:100px;top:232px;font-size:11px">(75mins of serious grooming)</div>
    <div class="abs" style="left:56px;top:302px;font-size:20px;font-weight:700;color:var(--orange);transform:rotate(-90deg);transform-origin:left top">with</div>
    <div class="abs head-big" style="left:84px;top:250px;font-size:54px">Brenna</div>
    <div class="abs" style="left:106px;top:314px;font-size:16px;color:var(--white);line-height:19px">Choose any<br><span style="color:var(--orange);font-weight:700">2 male treatments</span><br>from the following<br>menus for</div>
    <div class="abs" style="left:262px;top:392px;font-size:20px;font-weight:700;color:var(--orange);transform:rotate(-90deg);transform-origin:left top">just</div>
    <div class="abs price" style="left:294px;top:316px;font-size:72px"><sup>$</sup>99!</div>

    <div class="photo" role="img" aria-label="Portrait photo of Brenna, male grooming therapist" style="left:312px;top:47px;width:150px;height:225px;background:linear-gradient(160deg,#a99a86,var(--photo-warm) 55%,#3d3140)"></div>

    <div class="ornament" role="img" aria-label="Orange floral flourish" style="left:640px;top:0;width:140px;height:170px"></div>
    <div class="menu-box" style="left:499px;top:210px;width:243px;height:200px">
      <div class="menu-title" style="top:46px">BODY</div>
      <div class="menu-items" style="top:66px">• 30 minute deep tissue massage<br>• full body detox body scrub<br>• Mens maintenance pedicure<br>• Mens maintenance manicure</div>
      <div class="menu-title" style="top:145px">FACE</div>
    </div>
    <div class="badge" style="left:482px;top:40px;width:196px;height:196px;padding-top:30px">
      <div style="font-size:17px;font-weight:900;line-height:17px">OFFERED BY<br>APPOINTMENT<br>WITH BRENNA</div>
      <div style="font-size:9.5px;line-height:11.5px;margin:5px auto 0;width:136px">our Male grooming therapist only various days and times subject to availability, subject to change without notice; limitless services per customer</div>
    </div>
  </div>
  <div class="footer">
    <div class="brand-name">velquora</div>
    <div class="address">Shop 4, 212 Harlow Street<br>KELVERTON QLD 4170</div>
    <div class="phone">(07) 3946 0582</div>
    <div class="email">Email: <b>info@velquorastudio.net.au</b></div>
    <div class="divider"></div>
    <div class="hours">
      <h3>Hours of Operation</h3>
      Mon - Tues: 8:00am - 5:30pm<br>Wed - Thurs: 8:00am - 8:00pm<br>Fri: 8:00am - 5:30pm<br>Sat : 8:00am - 4:00pm
      <div class="closed">Sundays &amp; Public Holidays:<br>CLOSED</div>
    </div>
  </div>
</section>

<section class="flyer flyer--colour">
  <div class="panel">
    <div class="abs head-thin" style="left:65px;top:40px;font-size:46px">Marlows</div>
    <div class="abs head-big" style="left:42px;top:70px;font-size:104px">colour</div>
    <div class="abs head-big" style="left:84px;top:140px;font-size:104px">bar</div>
    <div class="abs small-note" style="left:116px;top:232px">(available Tues - Thurs)</div>
    <div class="abs price" style="left:50px;top:244px;font-size:92px"><sup>$</sup>99!</div>

    <div class="ornament" role="img" aria-label="Orange floral flourish" style="left:345px;top:20px;width:170px;height:170px"></div>

    <div class="badge" style="left:269px;top:155px;width:226px;height:226px;padding-top:20px">
      <div style="font-size:22px;font-weight:900;line-height:22px">AVAILABLE<br>FOR LIMITED<br>TIMES</div>
      <div style="font-size:13px;font-weight:700;line-height:18px;margin-top:6px">Sept 16 - Nov 6 2014<br>Dec 30-Feb 27 with Marlow</div>
      <div style="font-size:11px;line-height:14px">only and for one service per<br>customer at advertised price of</div>
      <div class="price" style="font-size:40px;line-height:40px;margin-top:2px"><sup>$</sup>99!</div>
    </div>

    <ul class="benefits" style="left:520px;top:53px;font-size:16px;line-height:21px">
      <li style="margin-bottom:4px">Freshen up your look in<br>the experienced hands of<br>a Senior Stylist</li>
      <li style="margin-bottom:4px">1/2 head of foils or regrowth colour</li>
      <li style="margin-bottom:4px">Precision style cut and Blowdry</li>
      <li>Appointments after 4pm<br>enjoy a complimentry glass of wine</li>
    </ul>
  </div>
  <div class="footer">
    <div class="brand-name">velquora</div>
    <div class="address">Shop 4, 212 Harlow Street<br>KELVERTON QLD 4170</div>
    <div class="phone">(07) 3946 0582</div>
    <div class="email">Email: <b>info@velquorastudio.net.au</b></div>
    <div class="divider"></div>
    <div class="hours">
      <h3>Hours of Operation</h3>
      Mon - Tues: 8:00am - 5:30pm<br>Wed - Thurs: 8:00am - 8:00pm<br>Fri: 8:00am - 5:30pm<br>Sat : 8:00am - 4:00pm
      <div class="closed">Sundays &amp; Public Holidays:<br>CLOSED</div>
    </div>
  </div>
  <div class="photo" role="img" aria-label="Portrait photo of Marlow, senior stylist" style="left:547px;top:273px;width:228px;height:295px;background:linear-gradient(165deg,#4a3a3c,var(--photo-cool) 40%,#a08888 70%,#2a2224)"></div>
</section>

</body>
</html>
```